Napa Winery Zinfandel label

We are a new start-up winery of high-end Napa wine. The label is to be silk screened or etched into the bottle. This initial logo is for the Velvet Ember Wine Co. Zinfandel wine.

The attached is an idea I would like followed for general guidance, meant to depict a "carnal sin" and sensual as per attached image.

Looking for some new ideas.....subtle sexy but risqué preferred! Silhouette in white and red writing of "Velvet zin" is what we are hoping for....

Please depict on a wine bottle (red wine) or near black background.

Thank you.

Font styles to use
Other font styles liked:
• colonna mt

Colors
f04950
ffffff

Requirements
Must have
• Female silhouette - risqué
Nice to have
• sensual - edgy
Should not have
• gold

```html
<!DOCTYPE html>
<html lang="en">
<head>
<meta charset="utf-8">
<title>Velvet Ember Wine Co. – Velvet Zin Label</title>
<link rel="stylesheet" href="https://fonts.googleapis.com/css2?family=Tulpen+One&family=PT+Sans&display=swap">
<style>
  :root {
    --bottle-dark: #141012;
    --bottle-deep: #1e1416;
    --ember-red: #f04950;
    --wine-red: #7a1a20;
    --label-white: #ffffff;
    --soft-white: #d9d4d5;
  }
  * { margin: 0; padding: 0; box-sizing: border-box; }
  html, body {
    width: 1200px;
    height: 800px;
    overflow: hidden;
    background: var(--bottle-dark);
  }
  .label {
    position: relative;
    width: 1200px;
    height: 800px;
    overflow: hidden;
    background: linear-gradient(90deg, var(--bottle-dark) 0%, var(--bottle-deep) 100%);
  }
  .silhouette-art {
    position: absolute;
    left: 660px;
    top: 0;
    width: 480px;
    height: 800px;
    border-radius: 240px 240px 0 0;
    background: radial-gradient(ellipse at 50% 40%, var(--ember-red) 0%, var(--wine-red) 60%, var(--bottle-deep) 100%);
    opacity: 0.85;
  }
  .wordmark {
    position: absolute;
    left: 90px;
    top: 110px;
    font-family: "Tulpen One", sans-serif;
    font-weight: 400;
    line-height: 1;
  }
  .wordmark__name {
    display: block;
    font-size: 300px;
    letter-spacing: 8px;
    color: var(--ember-red);
  }
  .wordmark__varietal {
    display: block;
    margin-top: -10px;
    font-size: 160px;
    letter-spacing: 8px;
    color: var(--label-white);
  }
  .company {
    position: absolute;
    left: 96px;
    top: 595px;
    font-family: "PT Sans", sans-serif;
    font-size: 32px;
    color: var(--label-white);
  }
  .origin {
    position: absolute;
    left: 96px;
    top: 660px;
    font-family: "PT Sans", sans-serif;
    color: var(--soft-white);
  }
  .origin__region { display: block; font-size: 28px; }
  .origin__vintage { display: block; font-size: 22px; margin-top: 4px; }
</style>
</head>
<body>
  <main class="label">
    <div class="silhouette-art" role="img" aria-label="Red brush-line drawing of a female silhouette seen from behind"></div>
    <h1 class="wordmark">
      <span class="wordmark__name">Velvet</span>
      <span class="wordmark__varietal">Zin</span>
    </h1>
    <p class="company">Velvet Ember Wine Co.</p>
    <p class="origin">
      <span class="origin__region">Napa Valley</span>
      <span class="origin__vintage">2015</span>
    </p>
  </main>
</body>
</html>
```